Exciting Poster Project: 4 posters for Employee Benefit Program

We are an entrepreneurial healthcare IT company that is creating an internal campaign to launch our 2017 Culture and Professional Development goals for our internal staff.

We need 4 posters utilizing the 4 campaign logos (attached) that are tied together visually into a cohesive campaign.

A PPT is included that shows the other wall art that currently exists on the walls. The new posters will share a space with these pieces.

The posters may be mounted side by side, or stand alone on a wall- so the design should work both ways. Each poster should include its own icon and the tag line provided along with topics provided that fall under this category. The posters size can be dictated by your design, but the text should be legible from a minimum of 8 feet away.

At the bottom of each poster should include all 4 icons in order to tie the entire campaign together (perhaps they can be arranged together like a diamond shape with the primary one as the biggest diamond)

Our company website for our external branding is: www.pelmaroq.com
We have included our branding guidelines for our external brand, and ppts and graphics for our internal brand.

1) Poster 1:
a. Header: Better Today Than Yesterday
b. Sub-title: Personal and Professional Growth
c. Description: We are committed to helping you build on your strengths and passions and support you your career advancement goals. We have a variety of training and development programs available to help you reach your top potential!
Leadership Development Programs
1. Supervisor Training
2. Women’s Leadership
3. Leadership Meet-Ups
4. MBA Program
Staff Development
1. Continuing Education Fund
2. Book Club
3. Pelmaroq University
4. Mentorship
5. Learning Libraries
6. Department Wide Training Events

2) Poster 2:
a. Header: Perform at Highest Capacity
b. Sub-title: Be Your Best Self
c. Description: We are committed to providing programs that bring focus to your health and overall personal wellness to encourage a well balanced life
i. Healthy Living
1. Health and wellness seminars
2. Nutrition: Fruit Delivery
ii. Fitness:
1. Step Challenge
2. Virtual 5k
3. Recess
4. Golf Lessons
5. Ping Pong Club
iii. Creativity:
1. Painting
2. Photography Club
3. Virtual Trivia
iv. Mental Health:
1. Massage Therapy
2. EAP Education
v. Financial
1. 401(k)
2. Retirement education/financial planning seminars
3. Global Insurance Program education

3) Poster 3:
a. Header: Passionate Urgent and Driven to Success
b. Sub-Header: Innovation and Strategy
c. Description: We are committed to helping you connect the dots both in the industry and with our internal goals , mission, and vision.
i. Quarterly All-Hands
ii. Lumiverse
1. Internally: Departmental and Product Updates
2. Externally: Industry Knowledge
3. Culturally: Peer to Peer Community

4) Poster 4:
a. Header: Succeed as a Team
b. Sub-Header: Cultivating Collaboration
c. Description: We are committed to creating a culture of appreciation, teamwork, and supporting an open communication. All feedback and ideas are welcome here!
i. Team Building Events
1. Employee Focused
a. Summer Picnic
b. Employee Appreciation
c. Diwali
d. Holiday Party
e. Department Appreciation
2. Family Friendly
a. Halloween
b. Bring your Kids to Work Day
3. Awards
a. Peer to Peer: QuickNod Awards
b. Leadership: Crest of Merit
4. Surveys
a. New Hire
b. Employee Engagement
Updates

Target Market(s)

Internal Employees

Industry/Entity Type

Healthcare

Font styles to use
Sans Serif

Requirements
Must have
• Job Type: Posters
• Task Outline: Create Vector Art for 4 icons and 4 posters
• Fonts and Styles to Use: SourceSansPro
Nice to have
• There is an attachment with suggested concepts and styles that we like.
Should not have
• The poster should not be very wordy or hard to read in passing.

```html
<!DOCTYPE html>
<html lang="en">
<head>
<meta charset="utf-8">
<title>Passionate Urgent and Driven to Success — Innovation and Strategy</title>
<link rel="stylesheet" href="https://fonts.googleapis.com/css2?family=Source+Sans+3:wght@600;700;800;900&display=swap">
<style>
  :root {
    --teal: #0b8ba8;
    --teal-deep: #0a7893;
    --white: #ffffff;
    --magenta: #e5197a;
    --navy: #14234d;
    --ink: #0b1422;
    --orange: #ee5a24;
    --purple: #6e2c8e;
    --green: #8cc63f;
    --amber: #f7a035;
  }
  html, body { margin: 0; padding: 0; overflow: hidden; }
  body { width: 850px; height: 1200px; }
  .poster {
    position: relative;
    width: 850px;
    height: 1200px;
    overflow: hidden;
    background: var(--teal);
    font-family: "Source Sans 3", sans-serif;
  }
  .footer-band {
    position: absolute; left: 0; right: 0; top: 1118px; bottom: 0;
    background: var(--orange);
  }
  .diamond {
    position: absolute;
    transform: rotate(45deg);
    border-radius: 28px;
    box-sizing: border-box;
  }
  .diamond--outline { border: 3px solid var(--white); }
  .campaign-badge {
    left: 148px; top: 56px; width: 100px; height: 100px;
    background: var(--teal-deep);
    box-shadow: 4px 4px 12px rgba(0,0,0,0.25);
    border-radius: 20px;
  }
  .campaign-badge-dot {
    position: absolute; left: 180px; top: 88px; width: 36px; height: 36px;
    border: 4px solid var(--white); border-radius: 50%; box-sizing: border-box;
  }
  .title-rule {
    position: absolute; left: 308px; top: 48px; width: 5px; height: 116px;
    background: var(--white);
  }
  .headline {
    position: absolute; left: 340px; top: 50px; margin: 0;
    font-weight: 700; letter-spacing: 1px; line-height: 1;
  }
  .headline-line1 { display: block; font-size: 44px; color: var(--white); }
  .headline-line1 .accent { color: var(--magenta); }
  .headline-line2 { display: block; margin-top: 12px; margin-left: 28px; color: var(--navy); }
  .headline-line2 .small { font-size: 28px; }
  .headline-line2 .and { color: var(--ink); }
  .headline-line2 .big { font-size: 42px; }
  .subheader {
    position: absolute; left: 0; right: 0; top: 224px; margin: 0;
    text-align: center;
    font-size: 30px; font-weight: 700; color: var(--white); letter-spacing: 1px;
  }
  .dart-illustration {
    position: absolute; left: 352px; top: 352px; width: 150px; height: 500px;
    border-radius: 30px;
    background: linear-gradient(180deg, rgba(217,31,58,0.55) 0%, rgba(217,31,58,0.35) 50%, rgba(160,160,170,0.35) 80%, rgba(217,31,58,0.3) 100%);
  }
  .program-card--lumiverse { left: 51px; top: 324px; width: 250px; height: 250px; }
  .program-card--allhands { left: 580px; top: 561px; width: 195px; height: 195px; }
  .program-card--mission { left: 48px; top: 870px; width: 210px; height: 210px; }
  .card-text {
    position: absolute; margin: 0; text-align: center; color: var(--ink);
    font-family: "Source Sans 3", sans-serif; font-weight: 800;
    font-variant: small-caps;
  }
  .lumiverse-tab {
    position: absolute; left: 26px; top: 387px; margin: 0;
    transform: rotate(-45deg); transform-origin: left bottom;
    font-weight: 900; font-size: 23px; line-height: 1;
    font-variant: small-caps;
    color: var(--ink); letter-spacing: 0.5px;
  }
  .lumiverse-topics { left: 80px; top: 340px; width: 196px; font-size: 20px; line-height: 1.2; }
  .lumiverse-topics dt { margin: 0; }
  .lumiverse-topics dd { margin: 0 0 8px; }
  .allhands-label { left: 552px; top: 640px; width: 252px; font-size: 24px; }
  .mission-text { left: 58px; top: 928px; width: 190px; font-size: 15px; line-height: 1.35; }
  .icon-set .diamond { border-radius: 22px; box-shadow: 3px 3px 8px rgba(0,0,0,0.25); }
  .icon-wellness { left: 618px; top: 984px; width: 95px; height: 95px; background: var(--purple); }
  .icon-team { left: 528px; top: 1062px; width: 112px; height: 112px; background: var(--green); }
  .icon-connect { left: 702px; top: 1070px; width: 95px; height: 95px; background: var(--amber); }
</style>
</head>
<body>
<main class="poster">
  <div class="footer-band"></div>

  <div class="diamond campaign-badge" aria-hidden="true"></div>
  <div class="campaign-badge-dot" aria-hidden="true"></div>

  <div class="title-rule"></div>
  <h1 class="headline">
    <span class="headline-line1">PASSIONATE <span class="accent">URGENT</span></span>
    <span class="headline-line2"><span class="small and">AND</span> <span class="small">DRIVEN TO</span> <span class="big">SUCCESS</span></span>
  </h1>

  <h2 class="subheader">INNOVATION AND STRATEGY</h2>

  <div class="dart-illustration" role="img" aria-label="Illustration of a red dart with a Success ribbon striking the centre of a target"></div>

  <div class="diamond diamond--outline program-card program-card--lumiverse"></div>
  <p class="lumiverse-tab">Lumiverse</p>
  <dl class="card-text lumiverse-topics">
    <dt>Internally:</dt><dd>Departmental and<br>Product Updates</dd>
    <dt>Externally:</dt><dd>Industry Knowledge</dd>
    <dt>Culturally:</dt><dd>Peer to Peer<br>Community</dd>
  </dl>

  <div class="diamond diamond--outline program-card program-card--allhands"></div>
  <p class="card-text allhands-label">Quarterly All-Hands</p>

  <div class="diamond diamond--outline program-card program-card--mission"></div>
  <p class="card-text mission-text">We are committed to helping you connect the dots both in the industry and with our internal goals, mission, and vision.</p>

  <div class="icon-set">
    <div class="diamond icon-wellness" role="img" aria-label="Campaign icon: Be Your Best Self"></div>
    <div class="diamond icon-team" role="img" aria-label="Campaign icon: Personal and Professional Growth"></div>
    <div class="diamond icon-connect" role="img" aria-label="Campaign icon: Succeed as a Team"></div>
  </div>
</main>
</body>
</html>
```